Where Did the River Turn: A Season of Mending

The book size is 6x9. I am more interested in an illustrative design like the one I have posted below with a picture of my face and then having elements in the background of a barn, a cross and my little girls eyes peaking out from behind the scenery.
"Where Did the River Turn… A Season of Mending" is a gripping memoir of resilience, faith, and courage. Lorelle Brantmoor’s journey pulls back the curtain on a ranch family fractured by addiction, abuse, and chaos, while revealing an extraordinary path to self-discovery and purpose.
Lorelle, her older sister Kimbra, and their three younger brothers grow up in a destabilizing environment where frequent moves and changing schools are routine. All the while, they navigate life in the shadow of their father’s addiction, schizophrenia, and violent outbursts. With dark secrets of sexual abuse and domestic violence lurking behind closed doors, the family seems trapped in a cycle of destruction.
Yet, Lorelle’s spirit remains unbroken. Anchored by her unshakable belief that God is her true father and Jesus her brother, she clings to her faith and a guiding philosophy she calls “the next right move”—a quiet force that propels her forward, even as those around her fall victim to their demons. As her siblings descend into addiction, incarceration, and heartbreak, Lorelle works to protect herself from the same fate while holding onto the family she cherishes.
Described by those who know her as possessing sophisticated grit, Lorelle rises above her circumstances with a unique blend of resilience, conscientiousness, and inner grace. She is driven by her belief in “organic truth”—the truth you possess before you are even born—which, once discovered, has the power to set you free into becoming who you were met to be. This profound conviction, along with her commitment to “the next right move,” guides her through life’s darkest moments.
Armed with a PhD in Human Science and experience as a child abuse and neglect investigator, therapist, professor, business leader and coach, Lorelle’s true triumph lies in something far deeper: surviving three near-death experiences and realizing that her purpose transcends personal, professional, and material achievements. Rather than pursuing happiness, she dedicates herself to uncovering meaning.
In this inspiring and candid memoir, she invites readers on a journey of becoming—one marked by faith, perseverance, and the courage to listen to the voice of organic truth within. Her story is a testament to the resilience of the human spirit and a beacon of hope for anyone navigating their own path to reclaim their sense of self, purpose, and freedom.

```html
<!DOCTYPE html>
<html lang="en">
<head>
<meta charset="utf-8">
<title>Where Did the River Turn – Cover</title>
<link rel="stylesheet" href="https://fonts.googleapis.com/css2?family=Playfair+Display:wght@400;500&family=Montserrat:wght@500&display=swap">
<style>
  :root {
    --page: #ffffff;
    --cover-yellow: #fbb800;
    --ink: #111111;
    --subtitle-red: #8b1a10;
    --art-charcoal: #2f2d33;
    --art-light: #fff3cf;
  }
  * { box-sizing: border-box; margin: 0; padding: 0; }
  html, body {
    width: 1200px;
    height: 1200px;
    overflow: hidden;
    background: var(--page);
  }
  .canvas {
    position: relative;
    width: 1200px;
    height: 1200px;
  }
  .cover {
    position: absolute;
    left: 240px;
    top: 60px;
    width: 720px;
    height: 1080px;
    background: var(--cover-yellow);
    overflow: hidden;
  }
  .cover-art {
    position: absolute;
    left: 200px;
    top: 430px;
    width: 660px;
    height: 700px;
  }
  .cover-subtitle {
    position: absolute;
    left: 52px;
    top: 92px;
    font-family: "Playfair Display", serif;
    font-weight: 400;
    font-size: 33px;
    line-height: 40px;
    color: var(--subtitle-red);
    text-transform: uppercase;
    letter-spacing: 0.5px;
  }
  .cover-title {
    position: absolute;
    left: 48px;
    top: 190px;
    font-family: "Playfair Display", serif;
    font-weight: 500;
    font-size: 128px;
    line-height: 124px;
    letter-spacing: -4px;
    color: var(--ink);
    text-transform: uppercase;
  }
  .cover-title span { display: block; }
  .cover-byline {
    position: absolute;
    left: 54px;
    top: 868px;
  }
  .byline-label {
    font-family: "Montserrat", sans-serif;
    font-weight: 500;
    font-size: 17px;
    letter-spacing: -0.3px;
    color: var(--ink);
    text-transform: uppercase;
    margin-bottom: 8px;
  }
  .byline-author {
    font-family: "Playfair Display", serif;
    font-weight: 400;
    font-size: 47px;
    line-height: 56px;
    letter-spacing: -0.5px;
    color: var(--ink);
    text-transform: uppercase;
  }
  .byline-author span { display: block; }
</style>
</head>
<body>
<div class="canvas">
  <section class="cover">
    <svg class="cover-art" viewBox="0 0 660 700" role="img" aria-label="Illustration: a white pawn standing before a tall dark bishop on a checkered board, with a halo of white dots behind them">
      <defs>
        <radialGradient id="artGlow" gradientUnits="userSpaceOnUse" cx="340" cy="360" r="310">
          <stop offset="0" stop-color="#2f2d33"/>
          <stop offset="0.35" stop-color="#2f2d33" stop-opacity="0.85"/>
          <stop offset="0.65" stop-color="#fff3cf" stop-opacity="0.45"/>
          <stop offset="1" stop-color="#fbb800" stop-opacity="0"/>
        </radialGradient>
      </defs>
      <rect x="0" y="0" width="660" height="700" fill="url(#artGlow)"/>
    </svg>

    <p class="cover-subtitle">A Season<br>of Mending</p>

    <h1 class="cover-title">
      <span>Where</span>
      <span>Did The</span>
      <span>River</span>
      <span>Turn</span>
    </h1>

    <div class="cover-byline">
      <p class="byline-label">A Memoir By</p>
      <p class="byline-author"><span>Lorelle</span><span>Brantmoor</span></p>
    </div>
  </section>
</div>
</body>
</html>
```